Bref créative
Velvet Rooms
Home Interiors
Modern
Linnea Parcot Weller
Design Consultant
412 Quillon Lane
Ferncastle Gardens, Ov 33587
LinneaParcot@velmorra.example
VelvetRooms.example
My logo is the Velvet Rooms. Would like to incorporate a flur de lis.

```html
<!DOCTYPE html>
<html lang="en">
<head>
<meta charset="utf-8">
<title>Velvet Rooms — Business Card</title>
<link rel="stylesheet" href="https://fonts.googleapis.com/css2?family=Caladea:wght@400;700&display=swap">
<style>
  :root {
    --backdrop: #e9e6e2;
    --card: #ffffff;
    --ink: #2b2b2b;
    --muted: #555555;
    --accent: #c8102e;
    --accent-dark: #9e0b22;
    --band-black: #111111;
    --rule: #d4d4d4;
  }
  * { box-sizing: border-box; margin: 0; padding: 0; }
  html, body {
    width: 1200px; height: 780px; overflow: hidden;
    background: var(--backdrop);
    font-family: "Caladea", Georgia, serif;
    color: var(--ink);
  }
  .card {
    position: absolute; left: 100px; top: 100px;
    width: 1000px; height: 580px;
    background: var(--card);
    border-radius: 34px;
    overflow: hidden;
    box-shadow: 0 10px 30px rgba(0,0,0,0.18);
  }
  .brand {
    position: absolute; left: 150px; top: 262px;
    display: flex; align-items: center; gap: 16px;
  }
  .brand-dot {
    width: 16px; height: 16px; border-radius: 50%;
    background: var(--accent);
  }
  .brand-name {
    font-size: 34px; font-weight: 400; line-height: 1.05;
    color: var(--muted); letter-spacing: 0.5px;
  }
  .divider {
    position: absolute; left: 420px; top: 60px;
    width: 2px; height: 340px;
    background: linear-gradient(to bottom, transparent, var(--rule) 15%, var(--rule) 85%, transparent);
  }
  .details { position: absolute; left: 450px; top: 60px; }
  .person-name { font-size: 32px; font-weight: 700; color: var(--accent); }
  .person-title { font-size: 19px; margin-top: 4px; }
  .address { font-size: 18px; line-height: 1.4; margin-top: 48px; }
  .contacts { list-style: none; margin-top: 34px; font-size: 18px; }
  .contacts li { display: flex; align-items: center; gap: 12px; height: 32px; }
  .contacts svg { width: 20px; height: 20px; fill: var(--accent); flex: none; }
  .swoosh { position: absolute; left: 0; bottom: 0; width: 1000px; height: 200px; }
</style>
</head>
<body>
  <div class="card">
    <div class="brand">
      <span class="brand-dot"></span>
      <span class="brand-name">Velvet<br>Rooms, LLC</span>
    </div>

    <div class="divider"></div>

    <div class="details">
      <h1 class="person-name">Linnea Parcot Weller</h1>
      <p class="person-title">Design Consultant</p>
      <p class="address">412 Quillon Lane<br>Ferncastle Gardens, Ov 33587</p>
      <ul class="contacts">
        <li>
          <svg viewBox="0 0 20 20" aria-hidden="true"><rect x="5" y="1" width="10" height="18" rx="2"/><rect x="7" y="3.5" width="6" height="8" fill="#fff"/></svg>
          555.014.2287
        </li>
        <li>
          <svg viewBox="0 0 20 20" aria-hidden="true"><rect x="2" y="8" width="16" height="10" rx="1.5"/><rect x="5" y="2" width="10" height="7" fill="none" stroke="#c8102e" stroke-width="2"/><rect x="5" y="12" width="10" height="2" fill="#fff"/></svg>
          555.017.3391
        </li>
        <li>
          <svg viewBox="0 0 20 20" aria-hidden="true"><circle cx="10" cy="10" r="8.5" fill="none" stroke="#c8102e" stroke-width="2.2"/><circle cx="10" cy="10" r="3.2" fill="none" stroke="#c8102e" stroke-width="2.2"/></svg>
          LinneaParcot@velmorra.example
        </li>
        <li>
          <svg viewBox="0 0 20 20" aria-hidden="true"><circle cx="10" cy="10" r="9"/><ellipse cx="10" cy="10" rx="3.5" ry="9" fill="none" stroke="#fff" stroke-width="1.2"/><line x1="1" y1="10" x2="19" y2="10" stroke="#fff" stroke-width="1.2"/></svg>
          VelvetRooms.example
        </li>
      </ul>
    </div>

    <svg class="swoosh" viewBox="0 0 1000 200" preserveAspectRatio="none" aria-hidden="true">
      <defs>
        <linearGradient id="red-band" x1="0" y1="0" x2="0" y2="1">
          <stop offset="0" stop-color="#d8182f"/>
          <stop offset="1" stop-color="#9e0b22"/>
        </linearGradient>
      </defs>
      <path d="M0 82 C 300 120, 650 90, 1000 20" fill="none" stroke="#bdbdbd" stroke-width="2"/>
      <path d="M0 95 C 300 135, 650 105, 1000 36 L1000 60 C 650 125, 300 150, 0 112 Z" fill="var(--band-black)"/>
      <path d="M0 112 C 300 150, 650 125, 1000 60 L1000 200 L0 200 Z" fill="url(#red-band)"/>
    </svg>
  </div>
</body>
</html>
```